Back Pain

Need a flyer similar to the attached draft. This is to be handed out to prospective patients. Note that Sketch Hive has already designed the logo. If you need a copy please contact me

```html
<!DOCTYPE html>
<html lang="en">
<head>
<meta charset="utf-8">
<title>Spine Ease Clinic – Tech Neck Flyer</title>
<link rel="stylesheet" href="https://fonts.googleapis.com/css2?family=Oswald:wght@400;500;600&family=Montserrat:wght@600;700&family=Open+Sans:wght@600;700&display=swap">
<style>
  :root {
    --page: #e9e9e9;
    --slate: #283842;
    --blue: #12b0e6;
    --blue-deep: #1b74c4;
    --green: #8cc63f;
    --white: #ffffff;
  }
  * { margin: 0; padding: 0; box-sizing: border-box; }
  html, body { width: 1071px; height: 1200px; overflow: hidden; background: var(--page); }
  .flyer {
    position: absolute; left: 108px; top: 0;
    width: 854px; height: 1200px;
    background: var(--slate);
    font-family: "Oswald", "Arial Narrow", sans-serif;
    overflow: hidden;
  }
  .abs { position: absolute; }
  .clinic-title {
    left: 0; width: 100%; top: 26px; text-align: center;
    font-family: "Montserrat", sans-serif; font-weight: 700; font-size: 39px; letter-spacing: 0.5px;
    background: linear-gradient(90deg, var(--blue-deep), var(--green));
    -webkit-background-clip: text; background-clip: text; color: transparent;
  }
  .headline {
    left: 0; width: 100%; top: 80px; text-align: center;
    font-weight: 600; font-size: 78px; line-height: 1; color: var(--green);
  }
  .walker {
    left: 86px; top: 179px; width: 210px; height: 692px;
    background: var(--blue); border-radius: 90px 90px 20px 20px;
  }
  .symptom {
    background: var(--green); color: var(--white);
    font-weight: 500; font-size: 20px; line-height: 1;
    display: flex; align-items: center; padding-left: 14px;
  }
  .chart-note {
    left: 490px; top: 198px; width: 230px;
    color: var(--blue); font-weight: 500; font-size: 19px; line-height: 1.2;
  }
  .chart { left: 0; top: 0; }
  .axis-labels {
    left: 480px; top: 410px; width: 256px; display: flex; justify-content: space-between;
    color: var(--white); font-weight: 500; font-size: 26px;
  }
  .axis-title { left: 470px; top: 448px; width: 270px; text-align: center; color: var(--blue); font-weight: 500; font-size: 15px; }
  .axis-side {
    left: 664px; top: 300px; width: 180px; text-align: center;
    transform: rotate(-90deg); color: var(--blue); font-weight: 500; font-size: 15px;
  }
  .head-icon { left: 480px; top: 282px; width: 54px; height: 68px; background: var(--blue); border-radius: 28px 28px 6px 12px; }
  .usage { left: 523px; top: 503px; color: var(--blue); font-weight: 500; }
  .usage .small { font-size: 19px; line-height: 1.3; }
  .usage .big { font-size: 31px; line-height: 1.1; }
  .claim { left: 306px; width: 548px; top: 628px; text-align: center; font-weight: 500; line-height: 1.2; }
  .claim .g { color: var(--green); }
  .claim .b { color: var(--blue); }
  .claim .l1 { font-size: 35px; }
  .claim .l2 { font-size: 25px; }
  .claim .l3 { font-size: 32px; }
  .brand { left: 0; width: 100%; top: 862px; display: flex; justify-content: center; align-items: center; gap: 12px; }
  .brand-dot { width: 34px; height: 34px; border-radius: 50%; background: var(--blue); }
  .brand-name { font-family: "Oswald", sans-serif; font-weight: 500; font-size: 26px; color: var(--blue); }
  .doctor { left: 0; width: 100%; top: 950px; text-align: center; color: var(--green); font-weight: 500; font-size: 60px; line-height: 1; }
  .address { left: 0; width: 100%; top: 1027px; text-align: center; color: var(--blue); font-weight: 500; font-size: 14px; }
  .offer { left: 0; width: 100%; top: 1058px; text-align: center; color: var(--white); font-family: "Open Sans", sans-serif; font-weight: 600; font-size: 24px; }
  .url-bar {
    left: 173px; top: 1103px; width: 510px; height: 44px; border-radius: 6px;
    background: linear-gradient(90deg, var(--green), var(--blue-deep));
    display: flex; align-items: center; justify-content: center;
    color: var(--white); font-family: "Open Sans", sans-serif; font-weight: 700; font-size: 24px;
  }
  .option-note { left: 0; width: 100%; top: 1160px; text-align: center; color: var(--white); font-family: "Open Sans", sans-serif; font-weight: 600; font-size: 22px; }
</style>
</head>
<body>
<main class="flyer">
  <h1 class="abs clinic-title">SPINE EASE CLINIC</h1>
  <h2 class="abs headline">TECH NECK</h2>

  <div class="abs walker" role="img" aria-label="Silhouette of a person walking while looking down at a phone"></div>

  <div class="abs symptom" style="left:257px;top:204px;width:136px;height:36px;">HEADACHES</div>
  <div class="abs symptom" style="left:261px;top:254px;width:115px;height:35px;">NECK PAIN</div>
  <div class="abs symptom" style="left:230px;top:299px;width:163px;height:37px;">SHOULDER PAIN</div>
  <div class="abs symptom" style="left:235px;top:346px;width:122px;height:36px;">BACK PAIN</div>
  <div class="abs symptom" style="left:230px;top:430px;width:177px;height:37px;">ARM &amp; HAND PAIN</div>
  <div class="abs symptom" style="left:230px;top:479px;width:114px;height:37px;">SCIATICA</div>

  <p class="abs chart-note">AS THE HEAD TITLS FORWARD.<br>MORE FORCE IS PLACED<br>ON THE SPINE</p>

  <svg class="abs chart" width="854" height="1200" viewBox="0 0 854 1200" aria-hidden="true">
    <g fill="#8cc63f">
      <rect x="484" y="376" width="39" height="28"/>
      <rect x="535" y="326" width="39" height="78"/>
      <rect x="588" y="286" width="39" height="118"/>
      <rect x="641" y="260" width="39" height="144"/>
      <rect x="694" y="226" width="39" height="178"/>
    </g>
    <circle cx="458" cy="546" r="50" fill="#8cc63f"/>
    <path d="M458 546 L458 496 A50 50 0 0 1 482 590 Z" fill="#12b0e6"/>
  </svg>
  <div class="abs head-icon" role="img" aria-label="Small head profile tilted forward"></div>

  <div class="abs axis-labels"><span>0°</span><span>15°</span><span>30°</span><span>45°</span><span>60°</span></div>
  <div class="abs axis-title">DEGREES OF FORWARD HEAD TILD</div>
  <div class="abs axis-side">PRESSURE ON SPINE (LBS)</div>

  <div class="abs usage">
    <div class="small">THE AVERAGE PERSON SPENDS</div>
    <div class="big">8-11 HOURS PER DAY</div>
    <div class="small">USING ELECTRONIC DEVICES</div>
  </div>

  <div class="abs claim">
    <div class="l1"><span class="g">CHIROPRACTIC CARE</span> <span class="b">CAN HELP</span></div>
    <div class="l2 b">CORRECT AND PREVENT THESE PROBLEMS</div>
    <div class="l3"><span class="b">BY</span> <span class="g">RESTORING</span> <span class="b">AND</span> <span class="g">MAINTAINING</span></div>
    <div class="l3"><span class="g">PROPER ALIGNMENT</span> <span class="b">OF THE NECK</span></div>
  </div>

  <div class="abs brand">
    <span class="brand-dot"></span>
    <span class="brand-name">SPINE EASE CLINIC</span>
  </div>

  <div class="abs doctor">DR MARTIN HALE</div>
  <div class="abs address">NOW IN SEAVIEW AT 42 HARBOUR RD - QUAY SUITES</div>
  <div class="abs offer">50% OFF INITIAL CONSULTATION IF NOW BOOK ON LINE AT</div>
  <div class="abs url-bar">www.spineeaseclinic.com.au</div>
  <div class="abs option-note">*CHOSE “TECH NECK” OPTION</div>
</main>
</body>
</html>
```